Update existing website to a one page design.

Combine a multi page website into a single page design.
Existing site is at ac.calmharborcover (dot) com.
Rearrange elements as needed to create a modem look.
Not every element / all of the text need to be kept, design should be flexible enough to allow for new text (of different length) to be used.
Site should have a clear calls to action, such as get a quote and contact us.
Ability, call to action, to switch to Russian should be clearly visible near the top, translation will not be done by google, thus attribution is not needed.
Unused features (such as blog) should be dropped.
Images, besides logos, can be brand new.
Site should adhere to standard design practices (such as grid) and ideally be compatible with existing framework (such as bootstrap).
Coding of the website will likely be done by the winning bidder as a separate project.

```html
<!DOCTYPE html>
<html lang="en">
<head>
<meta charset="utf-8">
<title>Calm Harbor Cover – One Page Website Design</title>
<link href="https://fonts.googleapis.com/css2?family=Saira:wght@600;700;800&family=Roboto:wght@400;500;700&display=swap" rel="stylesheet">
<style>
:root{
  --blue:#0a51a1;
  --blue-dark:#083f7e;
  --orange:#f78d03;
  --ink:#1d2433;
  --muted:#8a909b;
  --line:#e3e6ec;
  --board:#f1f2f4;
  --soft:#f4f6f9;
  --white:#ffffff;
}
*{box-sizing:border-box;margin:0;padding:0}
html,body{width:1200px;height:4766px;overflow:hidden}
body{background:var(--board);font-family:"Roboto",Arial,sans-serif;color:var(--ink);position:relative}
.abs{position:absolute}
.head-font{font-family:"Saira",Arial,sans-serif}
.photo{position:absolute}
.btn{display:inline-flex;align-items:center;gap:3px;background:var(--orange);color:#fff;font-weight:700;text-transform:uppercase;border-radius:2px;white-space:nowrap}
.btn::after{content:"";width:6px;height:6px;border-radius:50%;background:#fff;opacity:.9}
.blue{color:var(--blue)}

/* board */
.top-band{position:absolute;left:0;top:0;width:1200px;height:498px;background:var(--blue)}
.board-title{position:absolute;font-family:"Roboto",sans-serif;font-weight:500;color:var(--ink);text-align:center}
.swatch{position:absolute;width:90px;height:90px;border-radius:50%}
.swatch-label{position:absolute;width:120px;text-align:center;font-size:15px;font-weight:700;font-style:italic}
.font-chip{position:absolute;width:90px;height:90px;border-radius:50%;background:#fff;box-shadow:0 4px 14px rgba(0,0,0,.08);display:flex;align-items:center;justify-content:center;font-size:34px;font-weight:500}
.font-name{position:absolute;width:180px;text-align:center;font-size:11px;font-weight:500;letter-spacing:.5px}
.divider{position:absolute;left:612px;top:836px;width:1px;height:210px;background:#c9ccd2}
.version-title{position:absolute;font-family:"Roboto",sans-serif;font-weight:700;font-size:27px;letter-spacing:.5px}

/* preview cards */
.preview{position:absolute;background:#fff;overflow:hidden;box-shadow:0 10px 30px rgba(0,0,0,.18)}

/* desktop page */
.desk{position:absolute;left:131px;top:1258px;width:648px;height:3030px;background:#fff;overflow:hidden}
.nav-logo{display:flex;align-items:center;gap:5px;font-family:"Saira",sans-serif;font-weight:800;color:var(--blue);line-height:.9}
.nav-logo .mark{background:var(--blue);border-radius:50%}
.nav-links{display:flex;gap:14px;font-size:7px;color:var(--ink)}
.nav-links .active{color:var(--orange)}
.callus{display:flex;align-items:center;gap:5px;font-size:6px;color:var(--muted)}
.callus b{display:block;font-size:9px;color:var(--ink)}
.hero-title{font-family:"Saira",sans-serif;font-weight:800;color:var(--blue);line-height:.95;text-transform:uppercase}
.hero-text{color:var(--ink)}
.eyebrow{font-size:8px;color:var(--blue);font-weight:700}
.sec-title{font-family:"Saira",sans-serif;font-weight:800;text-transform:uppercase;color:var(--ink)}
.body-copy{font-size:6.4px;line-height:9.5px;color:var(--muted);text-align:justify}
.svc{position:absolute;left:0;width:648px;height:218px}
.svc .photo{top:0;width:324px;height:218px}
.svc .txt{position:absolute;top:0;width:324px;height:218px;padding:0 62px 0 48px;display:flex;flex-direction:column;justify-content:center;gap:8px}
.svc .txt h3{font-family:"Saira",sans-serif;font-weight:700;font-size:13px;text-transform:uppercase;color:var(--ink)}
.svc .badge{position:absolute;top:95px;left:304px;width:40px;height:40px;border-radius:50%;background:var(--blue);border:3px solid #fff;display:flex;align-items:center;justify-content:center;z-index:2}
.ticks{list-style:none;display:flex;flex-direction:column;gap:5px;font-size:6.4px;color:var(--muted)}
.ticks li{display:flex;align-items:center;gap:5px}
.ticks li::before{content:"";width:6px;height:6px;border-radius:50%;background:var(--orange)}
.field{height:18px;border:1px solid var(--line);background:#fafbfc;font-size:6px;color:var(--muted);padding:5px 6px}
.partner{width:80px;height:42px;background:#fff;border-radius:4px;box-shadow:0 2px 8px rgba(0,0,0,.08);display:flex;align-items:center;justify-content:center}
.partner span{display:block;width:48px;height:12px;border-radius:6px}
.arrow-dot{width:16px;height:16px;border-radius:50%;background:#fff;box-shadow:0 1px 4px rgba(0,0,0,.15);display:flex;align-items:center;justify-content:center;font-size:9px;color:var(--ink)}
.foot-col h4{font-size:8px;color:#fff;font-weight:700;margin-bottom:8px}
.foot-col p{font-size:6.4px;color:#dbe6f5;line-height:10px}
.social{display:flex;gap:4px}
.social i{width:12px;height:12px;border-radius:50%;border:1px solid #fff;display:block}

/* mobile page */
.mob{position:absolute;left:884px;top:1258px;width:161px;height:3380px;background:#fff;overflow:hidden}
.mob .body-copy{font-size:4.2px;line-height:6.4px}
.mob .btn{font-size:4.6px;padding:3px 6px}
.mob .btn::after{width:4px;height:4px}
.m-h{font-family:"Saira",sans-serif;font-weight:700;text-transform:uppercase;color:var(--ink);font-size:6px}
.m-field{height:12px;border:1px solid var(--line);background:#fafbfc;font-size:4px;color:var(--muted);padding:3px 4px;margin-bottom:5px}
.m-icon{width:24px;height:24px;border-radius:50%;border:1.5px solid var(--blue);display:flex;align-items:center;justify-content:center}
.m-icon span{width:12px;height:12px;border-radius:50%;background:var(--blue)}
.m-label{font-size:4.2px;text-align:center;color:var(--ink);margin-top:3px;line-height:5.5px}
</style>
</head>
<body>

<svg width="0" height="0" style="position:absolute">
  <symbol id="i-phone" viewBox="0 0 24 24"><path d="M6.6 10.8a15 15 0 0 0 6.6 6.6l2.2-2.2a1 1 0 0 1 1-.25 11.4 11.4 0 0 0 3.6.57 1 1 0 0 1 1 1V20a1 1 0 0 1-1 1A17 17 0 0 1 3 4a1 1 0 0 1 1-1h3.5a1 1 0 0 1 1 1c0 1.25.2 2.45.57 3.57a1 1 0 0 1-.25 1z" fill="currentColor"/></symbol>
  <symbol id="i-pin" viewBox="0 0 24 24"><path d="M12 2a7 7 0 0 0-7 7c0 5.2 7 13 7 13s7-7.8 7-13a7 7 0 0 0-7-7zm0 9.5A2.5 2.5 0 1 1 12 6.5a2.5 2.5 0 0 1 0 5z" fill="currentColor"/></symbol>
  <symbol id="i-mail" viewBox="0 0 24 24"><path d="M3 5h18v14H3z" fill="none" stroke="currentColor" stroke-width="2"/><path d="M3 6l9 7 9-7" fill="none" stroke="currentColor" stroke-width="2"/></symbol>
  <symbol id="i-plus" viewBox="0 0 24 24"><rect x="4" y="4" width="16" height="16" rx="3" fill="none" stroke="currentColor" stroke-width="2"/><path d="M12 8v8M8 12h8" stroke="currentColor" stroke-width="2"/></symbol>
  <symbol id="i-search" viewBox="0 0 24 24"><circle cx="10" cy="10" r="6" fill="none" stroke="currentColor" stroke-width="2.5"/><path d="M15 15l5 5" stroke="currentColor" stroke-width="2.5"/></symbol>
</svg>

<!-- ================= HERO SHOWCASE ================= -->
<div class="top-band"></div>

<section class="preview" style="left:222px;top:228px;width:760px;height:440px">
  <div class="abs" style="left:82px;top:30px" >
    <div class="nav-logo" style="font-size:11px"><span class="mark" style="width:18px;height:18px"></span>CALM<br>HARBOR</div>
  </div>
  <div class="abs callus" style="left:400px;top:24px;font-size:8px"><svg width="14" height="14" style="color:var(--blue)"><use href="#i-phone"/></svg><div>Call Us Today<b style="font-size:12px">877-555-0142</b></div></div>
  <div class="abs btn" style="left:550px;top:26px;font-size:8px;padding:6px 10px;text-transform:none">Get An Instant Quote</div>
  <nav class="abs nav-links" style="left:232px;top:62px;font-size:8px"><span class="active">Home</span><span>About Us</span><span>What We Do</span><span>Our Services</span><span>Doctors Network</span><span>Contact Us</span><svg width="9" height="9"><use href="#i-search"/></svg><span>Eng ▾</span></nav>
  <div class="photo" role="img" aria-label="Smiling couple outdoors in summer clothing" style="left:70px;top:80px;width:260px;height:330px;background:linear-gradient(160deg,#c9b79a,#e3d3bb 45%,#f0ece4)"></div>
  <div class="abs hero-title" style="left:340px;top:150px;font-size:32px">Calm Harbor<br>Cover</div>
  <p class="abs hero-text" style="left:340px;top:228px;width:290px;font-size:9px;line-height:14px">Calm Harbor Cover Corporation is an Independent Insurance and Financial Brokerage Firm serving</p>
  <div class="abs btn" style="left:340px;top:272px;font-size:8px;padding:7px 12px">Get Started</div>
  <svg class="abs" style="left:0;top:330px" width="760" height="110" viewBox="0 0 760 110"><path d="M0 90 C200 110 420 70 760 10 L760 110 L0 110Z" fill="#fff"/><path d="M0 92 C220 112 430 70 760 8" fill="none" stroke="var(--orange)" stroke-width="3"/><path d="M0 98 C230 118 440 78 760 20 L760 32 C440 90 240 122 0 106Z" fill="var(--blue)"/></svg>
</section>

<section class="preview" style="left:868px;top:322px;width:186px;height:370px;border-radius:14px">
  <div class="abs" style="left:14px;top:12px"><div class="nav-logo" style="font-size:6px"><span class="mark" style="width:10px;height:10px"></span>CALM</div></div>
  <div class="abs" style="right:14px;top:14px;width:8px;height:6px;border-top:1.5px solid var(--ink);border-bottom:1.5px solid var(--ink)"></div>
  <div class="abs hero-title" style="left:0;width:186px;top:52px;text-align:center;font-size:10px">Calm Harbor Cover</div>
  <p class="abs" style="left:30px;width:126px;top:68px;text-align:center;font-size:5px;line-height:7px;font-weight:700">Calm Harbor Cover Corporation is an Independent Insurance and Financial Brokerage Firm serving</p>
  <div class="abs btn" style="left:62px;top:96px;font-size:5px;padding:4px 7px">Get Started</div>
  <div class="photo" role="img" aria-label="Smiling couple outdoors" style="left:20px;top:116px;width:146px;height:110px;background:linear-gradient(160deg,#c9b79a,#efe7da)"></div>
  <svg class="abs" style="left:0;top:200px" width="186" height="40" viewBox="0 0 186 40"><path d="M0 30 C70 40 120 20 186 4" fill="none" stroke="var(--orange)" stroke-width="2"/><path d="M0 34 C70 44 120 26 186 10 L186 16 C120 32 70 48 0 40Z" fill="var(--blue)"/></svg>
  <div class="abs eyebrow" style="left:16px;top:260px;font-size:5px">ABOUT US</div>
  <div class="abs m-h" style="left:16px;top:268px;font-size:7px">Calm Harbor Cover</div>
  <p class="abs body-copy" style="left:16px;top:282px;width:154px;font-size:4.2px;line-height:6.6px">Calm Harbor Cover Corporation is an Independent Insurance and Financial Brokerage Firm serving clients throughout Florida and internationally. We are an experienced team of professionals, committed to our primary mission to find the best insurance coverage for protection you want.</p>
</section>

<!-- ================= PALETTE & FONTS ================= -->
<div class="board-title" style="left:240px;top:840px;width:360px;font-size:40px">Color Pallet</div>
<div class="swatch" style="left:308px;top:924px;background:var(--blue)"></div>
<div class="swatch" style="left:437px;top:924px;background:var(--orange)"></div>
<div class="swatch-label" style="left:293px;top:1020px;color:var(--blue)">#0a51a1</div>
<div class="swatch-label" style="left:422px;top:1020px;color:var(--orange)">#f78d03</div>
<div class="divider"></div>
<div class="board-title" style="left:650px;top:840px;width:280px;font-size:40px">Fonts</div>
<div class="font-chip head-font" style="left:684px;top:924px">Aa</div>
<div class="font-chip" style="left:814px;top:924px">Aa</div>
<div class="font-name" style="left:639px;top:1024px">SAIRA</div>
<div class="font-name" style="left:769px;top:1024px">ROBOTO</div>

<div class="version-title" style="left:250px;top:1186px;width:410px;text-align:center">DESKTOP VERSION</div>
<div class="version-title" style="left:830px;top:1188px;width:270px;text-align:center;font-size:25px">MOBILE VERSION</div>

<!-- ================= DESKTOP PAGE ================= -->
<main class="desk">
  <!-- header -->
  <div class="abs" style="left:78px;top:14px"><div class="nav-logo" style="font-size:9px"><span class="mark" style="width:16px;height:16px"></span>CALM<br>HARBOR</div></div>
  <div class="abs callus" style="left:365px;top:10px"><svg width="12" height="12" style="color:var(--blue)"><use href="#i-phone"/></svg><div>Call Us Today<b>877-555-0142</b></div></div>
  <div class="abs btn" style="left:478px;top:12px;font-size:6.5px;padding:4px 8px;text-transform:none">Get An Instant Quote</div>
  <nav class="abs nav-links" style="left:186px;top:47px;font-size:6.5px"><span class="active">Home</span><span>About Us</span><span>What We Do</span><span>Our Services</span><span>Doctors Network</span><span>Contact Us</span><svg width="8" height="8"><use href="#i-search"/></svg><span>Eng ▾</span></nav>

  <!-- hero -->
  <div class="photo" role="img" aria-label="Smiling couple outdoors in summer clothing" style="left:0;top:60px;width:312px;height:270px;background:linear-gradient(160deg,#bca88a,#dfcfb5 45%,#f3efe8)"></div>
  <h1 class="abs hero-title" style="left:324px;top:118px;font-size:26px">Calm Harbor<br>Cover</h1>
  <p class="abs hero-text" style="left:324px;top:182px;width:270px;font-size:7px;line-height:11px">Calm Harbor Cover Corporation is an Independent Insurance and Financial Brokerage Firm serving</p>
  <div class="abs btn" style="left:324px;top:222px;font-size:6.5px;padding:5px 9px">Get Started</div>
  <svg class="abs" style="left:0;top:250px" width="648" height="100" viewBox="0 0 648 100"><path d="M0 70 C180 100 380 70 648 0 L648 100 L0 100Z" fill="#fff"/><path d="M0 74 C190 104 390 72 648 -2" fill="none" stroke="var(--orange)" stroke-width="3"/><path d="M0 80 C200 112 400 80 648 8 L648 20 C400 92 200 124 0 92Z" fill="var(--blue)"/></svg>

  <!-- about -->
  <section>
    <div class="abs eyebrow" style="left:78px;top:420px">ABOUT US</div>
    <h2 class="abs sec-title" style="left:78px;top:430px;font-size:13px;font-weight:700">Calm Harbor Cover</h2>
    <p class="abs body-copy" style="left:78px;top:452px;width:230px">Calm Harbor Cover Corporation is an Independent Insurance and Financial Brokerage Firm serving clients throughout Florida and internationally. We are an experienced team of professionals, committed to our primary mission – to find the best insurance coverage, for protection you want, at the best rate you deserve.</p>
    <p class="abs body-copy" style="left:78px;top:520px;width:230px">Our integrated suite of online services facilitates a comprehensive search and review of leading insurance companies.</p>
    <div class="abs btn" style="left:78px;top:548px;font-size:6px;padding:5px 9px">Load More</div>
    <div class="abs" style="left:398px;top:430px;width:140px;height:140px;border-radius:50%;background:var(--soft);border:2px solid var(--blue);display:flex;align-items:center;justify-content:center">
      <span class="head-font" style="font-weight:800;color:var(--blue);font-size:14px;text-align:center;line-height:1">CALM<br>HARBOR</span>
    </div>
  </section>

  <!-- what we do -->
  <h2 class="abs sec-title" style="left:0;width:648px;top:676px;text-align:center;font-size:17px">What <span class="blue">We Do</span></h2>

  <div class="svc" style="top:715px">
    <div class="photo" role="img" aria-label="Doctor consulting with a senior patient" style="left:0;background:linear-gradient(120deg,#dfe5ea,#c9cdd3 50%,#e2b7bb)"></div>
    <div class="badge"><svg width="16" height="16" style="color:#fff"><use href="#i-plus"/></svg></div>
    <div class="txt" style="left:324px">
      <h3>Individual Health</h3>
      <ul class="ticks"><li>Major Medical</li><li>Dental Insurance</li><li>Health Insurance for Foreign Nationals</li><li>Worldwide Health Insurance</li><li>Long Term Care Insurance (LTC) and Critical Illness Insurance</li><li>Medicare Advantage Plans</li></ul>
      <div class="btn" style="font-size:6px;padding:5px 9px;align-self:flex-start">Load More</div>
    </div>
  </div>

  <div class="svc" style="top:933px">
    <div class="txt" style="left:0;padding:0 48px 0 78px">
      <h3>Group Health Insurance</h3>
      <p class="body-copy">There was a time in generations past when simply holding down a full-time position with your community employer meant having the medical benefits you needed. Such was the nature of the social contract that came with the job. Health insurance and sound retirement planning were available, accessible and affordable. Visit your doctor, see the pharmacist to fill prescriptions.</p>
      <div class="btn" style="font-size:6px;padding:5px 9px;align-self:flex-start">Load More</div>
    </div>
    <div class="badge"><svg width="16" height="16" style="color:#fff"><use href="#i-plus"/></svg></div>
    <div class="photo" role="img" aria-label="Adviser meeting a senior couple at home" style="left:324px;background:linear-gradient(120deg,#eeeae4,#cfc7bd 55%,#8f8576)"></div>
  </div>

  <div class="svc" style="top:1151px">
    <div class="photo" role="img" aria-label="Happy couple on a white porch" style="left:0;background:linear-gradient(120deg,#e9e5dc,#c9b9a2 50%,#cf5a4f)"></div>
    <div class="badge"><svg width="16" height="16" style="color:#fff"><use href="#i-plus"/></svg></div>
    <div class="txt" style="left:324px">
      <h3>Life Insurance</h3>
      <p class="body-copy">We are specialists in all types of Life Insurance in all of Florida and even internationally. Consider these safety net vehicles as a vital piece of your long-term insurance strategy and estate planning. We will find the options that are the best fit for your funds which to choose.</p>
      <p class="body-copy">Renewable terms until the policy matures at age 120; it means that the insured person keeps the policy for the entire life.</p>
      <div class="btn" style="font-size:6px;padding:5px 9px;align-self:flex-start">Load More</div>
    </div>
  </div>

  <div class="svc" style="top:1369px">
    <div class="txt" style="left:0;padding:0 48px 0 78px">
      <h3>Pensions &amp; Annuities</h3>
      <p class="body-copy">Pension is often referred as Individual Retirement Account, known as IRA. It is an investing tool used by individuals to earn and earmark funds for retirement savings. There are several types of IRAs: Traditional IRAs, Roth IRAs, SIMPLE IRAs and SEP IRAs.</p>
      <p class="body-copy">Traditional and Roth IRAs are established by individual taxpayers, who are allowed to contribute.</p>
      <div class="btn" style="font-size:6px;padding:5px 9px;align-self:flex-start">Load More</div>
    </div>
    <div class="badge"><svg width="16" height="16" style="color:#fff"><use href="#i-plus"/></svg></div>
    <div class="photo" role="img" aria-label="Senior couple embracing on a beach" style="left:324px;background:linear-gradient(180deg,#8fc1da,#b8d8de 45%,#7fb8a8 70%,#d9cdb4)"></div>
  </div>

  <div class="svc" style="top:1587px">
    <div class="photo" role="img" aria-label="Warehouse aisles stacked with goods" style="left:0;background:linear-gradient(120deg,#7a4d24,#c98d3e 45%,#f0d69a 60%,#6b4322)"></div>
    <div class="badge"><svg width="16" height="16" style="color:#fff"><use href="#i-plus"/></svg></div>
    <div class="txt" style="left:324px">
      <h3>Property &amp; Commercial</h3>
      <p class="body-copy">Most South Florida residents love it here for our year-round tropical climate, and have long recognized owning a home as part of the Sunshine State's enviable lifestyle. But we fully understand that we live through days of unpredictable weather which can be added to excess.</p>
      <p class="body-copy">Hurricanes, plus tornadoes, flooding and fires are sobering events no matter their severity.</p>
      <div class="btn" style="font-size:6px;padding:5px 9px;align-self:flex-start">Load More</div>
    </div>
  </div>

  <!-- markets -->
  <section class="abs" style="left:0;top:1805px;width:648px;height:370px;background:var(--soft)">
    <h2 class="abs sec-title" style="left:0;width:648px;top:48px;text-align:center;font-size:17px">Our <span class="blue">Markets</span></h2>
    <svg class="abs" style="left:0;top:70px" width="648" height="300" viewBox="0 0 648 300">
      <g stroke="var(--blue)" stroke-width="1" fill="none">
        <circle cx="324" cy="150" r="80"/>
        <path d="M215 44 L262 90 M170 90 L244 130 M159 150 L244 150 M170 210 L244 170 M215 256 L262 210"/>
        <path d="M433 44 L386 90 M478 90 L404 130 M489 150 L404 150 M478 210 L404 170 M433 256 L386 210"/>
      </g>
      <circle cx="324" cy="150" r="50" fill="#fff" stroke="var(--blue)" stroke-width="2"/>
      <text x="324" y="148" text-anchor="middle" font-family="Saira, sans-serif" font-weight="800" font-size="11" fill="var(--blue)">CALM</text>
      <text x="324" y="161" text-anchor="middle" font-family="Saira, sans-serif" font-weight="800" font-size="11" fill="var(--blue)">HARBOR</text>
      <g fill="#fff" stroke="var(--blue)" stroke-width="1.5">
        <circle cx="215" cy="44" r="13"/><circle cx="170" cy="90" r="13"/><circle cx="159" cy="150" r="13"/><circle cx="170" cy="210" r="13"/><circle cx="215" cy="256" r="13"/>
        <circle cx="433" cy="44" r="13"/><circle cx="478" cy="90" r="13"/><circle cx="489" cy="150" r="13"/><circle cx="478" cy="210" r="13"/><circle cx="433" cy="256" r="13"/>
      </g>
      <g fill="var(--blue)">
        <circle cx="215" cy="44" r="5"/><circle cx="170" cy="90" r="5"/><circle cx="159" cy="150" r="5"/><circle cx="170" cy="210" r="5"/><circle cx="215" cy="256" r="5"/>
        <circle cx="433" cy="44" r="5"/><circle cx="478" cy="90" r="5"/><circle cx="489" cy="150" r="5"/><circle cx="478" cy="210" r="5"/><circle cx="433" cy="256" r="5"/>
      </g>
      <g font-family="Roboto, sans-serif" font-size="7" fill="var(--ink)" text-anchor="end">
        <text x="196" y="47">Auto</text><text x="151" y="93">Commercial</text><text x="140" y="153">Dental Insurance</text><text x="151" y="213">Disability</text><text x="196" y="259">Group Health Insurance</text>
      </g>
      <g font-family="Roboto, sans-serif" font-size="7" fill="var(--ink)">
        <text x="452" y="47">Homeowners</text><text x="497" y="89">Individual/Family Health</text><text x="497" y="98">Insurance</text><text x="508" y="149">Medicare Advantage</text><text x="508" y="158">Plans</text><text x="497" y="213">Medicare Supplements</text><text x="452" y="259">Pension &amp; Annuities</text>
      </g>
    </svg>
  </section>

  <!-- contact -->
  <section class="abs" style="left:0;top:2175px;width:648px;height:420px">
    <h2 class="abs sec-title" style="left:0;width:648px;top:44px;text-align:center;font-size:17px">Contact <span class="blue">Us</span></h2>
    <div class="abs" style="left:100px;top:84px;display:flex;gap:8px;align-items:flex-start"><svg width="22" height="22" style="color:var(--orange)"><use href="#i-pin"/></svg><div style="font-size:6px;color:var(--muted);line-height:8px"><b style="color:var(--ink);font-size:7px">LOCATION:</b><br>410 Harbor Lane<br>Seaview, FL 33000</div></div>
    <div class="abs" style="left:256px;top:84px;display:flex;gap:8px;align-items:flex-start"><svg width="22" height="22" style="color:var(--orange)"><use href="#i-phone"/></svg><div style="font-size:6px;color:var(--muted);line-height:8px"><b style="color:var(--ink);font-size:7px">PHONE:</b><br>954-555-0187</div></div>
    <div class="abs" style="left:404px;top:84px;display:flex;gap:8px;align-items:flex-start"><svg width="24" height="22" style="color:var(--orange)"><use href="#i-mail"/></svg><div style="font-size:6px;color:var(--muted);line-height:8px"><b style="color:var(--ink);font-size:7px">EMAIL:</b><br>info@calmharborcover.com</div></div>

    <div class="abs" style="left:78px;top:140px;width:234px">
      <h3 style="font-size:9px;font-weight:700;margin-bottom:3px">GET IN TOUCH</h3>
      <p style="font-size:6px;color:var(--muted);margin-bottom:12px">Reach out to us for any inquiry</p>
      <div class="field" style="margin-bottom:13px">First Name</div>
      <div class="field" style="margin-bottom:13px">Phone Number</div>
      <div class="field" style="margin-bottom:13px">Email Address</div>
      <div class="field" style="height:44px;margin-bottom:12px">Message</div>
      <div class="btn" style="width:234px;justify-content:center;font-size:6.5px;padding:6px 0">Submit</div>
    </div>
    <div class="photo" role="img" aria-label="Street map showing the office location" style="left:346px;top:138px;width:225px;height:228px;background:linear-gradient(135deg,#eef1ec,#e4e9e1 50%,#dfe6ee);border:4px solid #fff;box-shadow:0 2px 10px rgba(0,0,0,.12)"></div>
  </section>

  <!-- doctors network -->
  <section class="abs" style="left:0;top:2595px;width:648px;height:200px;background:var(--soft)">
    <h2 class="abs sec-title" style="left:0;width:648px;top:34px;text-align:center;font-size:17px">Doctors <span class="blue">Network</span></h2>
    <div class="abs" style="left:40px;top:78px;width:568px;display:flex;align-items:center;justify-content:space-between">
      <div class="arrow-dot">‹</div>
      <div class="partner"><span style="background:#f0a2a9"></span></div>
      <div class="partner"><span style="background:#3a3a3a"></span></div>
      <div class="partner"><span style="background:#4aa3c7"></span></div>
      <div class="partner"><span style="background:#5fa044"></span></div>
      <div class="partner"><span style="background:#1b2f5e"></span></div>
      <div class="arrow-dot">›</div>
    </div>
  </section>

  <!-- footer -->
  <footer class="abs" style="left:0;top:2795px;width:648px;height:235px">
    <svg class="abs" style="left:0;top:0" width="648" height="235" viewBox="0 0 648 235" preserveAspectRatio="none"><rect width="648" height="235" fill="var(--soft)"/><path d="M0 20 C180 -10 320 60 648 30 L648 235 L0 235Z" fill="var(--orange)"/><path d="M0 30 C180 2 320 70 648 42 L648 235 L0 235Z" fill="var(--blue)"/></svg>
    <div class="abs" style="left:88px;top:85px;text-align:center">
      <div class="nav-logo" style="font-size:13px;color:#fff;flex-direction:column;gap:4px"><span class="mark" style="width:24px;height:24px;background:#fff"></span>CALM<br>HARBOR</div>
      <div class="social" style="margin-top:8px"><i></i><i></i><i></i><i></i></div>
    </div>
    <div class="abs foot-col" style="left:220px;top:80px"><h4>Quick Links</h4><p>Home<br>About Us<br>What We Do<br>Our Services<br>Doctors Network<br>Contact Us</p></div>
    <div class="abs foot-col" style="left:333px;top:80px"><h4>About Company</h4><p>Legal Information<br>Terms &amp; Condition<br>Privacy Policy<br>Support<br>Site Map<br>FAQ</p></div>
    <div class="abs foot-col" style="left:451px;top:80px;width:120px"><h4>Contact Us</h4><p><b style="color:#fff">Phone</b><br>(813) 555-0166<br><b style="color:#fff">Email</b><br>info@calmharborcover.com<br><b style="color:#fff">Location</b><br>88 Pier Street, Seaview,<br>FL 33000</p></div>
    <div class="abs" style="left:0;width:648px;top:212px;text-align:center;font-size:6px;color:#dbe6f5">2021 Copyright - calmharborcover.com | All Rights Reserved</div>
    <div class="abs" style="left:580px;top:186px;width:16px;height:16px;border-radius:50%;background:var(--orange);color:#fff;font-size:8px;display:flex;align-items:center;justify-content:center">↑</div>
  </footer>
</main>

<!-- ================= MOBILE PAGE ================= -->
<main class="mob">
  <div class="abs" style="left:8px;top:8px"><div class="nav-logo" style="font-size:4.5px"><span class="mark" style="width:9px;height:9px"></span>CALM<br>HARBOR</div></div>
  <div class="abs" style="right:8px;top:12px;width:7px;height:6px;border-top:1.2px solid var(--ink);border-bottom:1.2px solid var(--ink)"></div>

  <h1 class="abs hero-title" style="left:0;width:161px;top:44px;text-align:center;font-size:7.5px">Calm Harbor Cover</h1>
  <p class="abs" style="left:22px;width:117px;top:56px;text-align:center;font-size:4.2px;line-height:6px;font-weight:700">Calm Harbor Cover Corporation is an Independent Insurance and Financial Brokerage Firm serving</p>
  <div class="abs btn" style="left:54px;top:86px">Get Started</div>
  <div class="photo" role="img" aria-label="Smiling couple outdoors" style="left:14px;top:104px;width:133px;height:120px;background:linear-gradient(160deg,#bca88a,#efe7da)"></div>
  <svg class="abs" style="left:0;top:200px" width="161" height="40" viewBox="0 0 161 40"><path d="M0 28 C60 38 110 20 161 4" fill="none" stroke="var(--orange)" stroke-width="1.5"/><path d="M0 32 C60 42 110 26 161 10 L161 15 C110 32 60 46 0 38Z" fill="var(--blue)"/></svg>

  <div class="abs eyebrow" style="left:12px;top:250px;font-size:4.2px">ABOUT US</div>
  <div class="abs m-h" style="left:12px;top:257px">Calm Harbor Cover</div>
  <p class="abs body-copy" style="left:12px;top:270px;width:137px">Calm Harbor Cover Corporation is an Independent Insurance and Financial Brokerage Firm serving clients throughout Florida and internationally.</p>
  <p class="abs body-copy" style="left:12px;top:296px;width:137px">We are an experienced team of professionals, committed to our primary mission – to find the best insurance coverage, for protection you want, at the best rate you deserve.</p>
  <div class="abs btn" style="left:12px;top:330px">Load More</div>
  <div class="abs" style="left:45px;top:400px;width:70px;height:70px;border-radius:50%;background:var(--soft);border:1.5px solid var(--blue);display:flex;align-items:center;justify-content:center"><span class="head-font" style="font-weight:800;color:var(--blue);font-size:7px;text-align:center;line-height:1">CALM<br>HARBOR</span></div>

  <h2 class="abs sec-title" style="left:0;width:161px;top:514px;text-align:center;font-size:7px">What <span class="blue">We Do</span></h2>

  <!-- service cards -->
  <div class="photo" role="img" aria-label="Doctor consulting with a senior patient" style="left:0;top:538px;width:161px;height:108px;background:linear-gradient(120deg,#dfe5ea,#c9cdd3 50%,#e2b7bb)"></div>
  <div class="abs" style="left:70px;top:636px;width:20px;height:20px;border-radius:50%;background:var(--blue);border:2px solid #fff"></div>
  <div class="abs m-h" style="left:12px;top:670px;font-size:4.5px">Individual Health</div>
  <ul class="abs ticks" style="left:12px;top:680px;gap:2px;font-size:4px"><li>Major Medical</li><li>Dental Insurance</li><li>Health Insurance for Foreign Nationals</li><li>Worldwide Health Insurance</li></ul>
  <div class="abs btn" style="left:12px;top:712px">Load More</div>

  <div class="photo" role="img" aria-label="Adviser meeting a senior couple" style="left:0;top:810px;width:161px;height:108px;background:linear-gradient(120deg,#eeeae4,#cfc7bd 55%,#8f8576)"></div>
  <div class="abs" style="left:70px;top:908px;width:20px;height:20px;border-radius:50%;background:var(--blue);border:2px solid #fff"></div>
  <div class="abs m-h" style="left:12px;top:942px;font-size:4.5px">Group Health Insurance</div>
  <p class="abs body-copy" style="left:12px;top:952px;width:100px">There was a time in generations past when simply holding down a full-time position with your community employer meant having the medical benefits you needed.</p>
  <div class="abs btn" style="left:12px;top:988px">Load More</div>

  <div class="photo" role="img" aria-label="Happy couple on a white porch" style="left:0;top:1082px;width:161px;height:108px;background:linear-gradient(120deg,#e9e5dc,#c9b9a2 50%,#cf5a4f)"></div>
  <div class="abs" style="left:70px;top:1180px;width:20px;height:20px;border-radius:50%;background:var(--blue);border:2px solid #fff"></div>
  <div class="abs m-h" style="left:12px;top:1214px;font-size:4.5px">Life Insurance</div>
  <p class="abs body-copy" style="left:12px;top:1224px;width:100px">We are specialists in all types of Life Insurance in all of Florida and even internationally. Consider these safety net vehicles as a vital piece of your long-term strategy.</p>
  <div class="abs btn" style="left:12px;top:1260px">Load More</div>

  <div class="photo" role="img" aria-label="Senior couple on a beach" style="left:0;top:1354px;width:161px;height:108px;background:linear-gradient(180deg,#8fc1da,#b8d8de 45%,#7fb8a8 70%,#d9cdb4)"></div>
  <div class="abs" style="left:70px;top:1452px;width:20px;height:20px;border-radius:50%;background:var(--blue);border:2px solid #fff"></div>
  <div class="abs m-h" style="left:12px;top:1486px;font-size:4.5px">Pensions &amp; Annuities</div>
  <p class="abs body-copy" style="left:12px;top:1496px;width:100px">Pension is often referred as Individual Retirement Account, known as IRA. It is an investing tool used by individuals to earn and earmark funds for retirement savings.</p>
  <div class="abs btn" style="left:12px;top:1532px">Load More</div>

  <div class="photo" role="img" aria-label="Warehouse aisles stacked with goods" style="left:0;top:1626px;width:161px;height:108px;background:linear-gradient(120deg,#7a4d24,#c98d3e 45%,#f0d69a 60%,#6b4322)"></div>
  <div class="abs" style="left:70px;top:1724px;width:20px;height:20px;border-radius:50%;background:var(--blue);border:2px solid #fff"></div>
  <div class="abs m-h" style="left:12px;top:1758px;font-size:4.5px">Property &amp; Commercial</div>
  <p class="abs body-copy" style="left:12px;top:1768px;width:100px">Most South Florida residents love it here for our year-round tropical climate, and see owning a home as part of the Sunshine State lifestyle.</p>
  <div class="abs btn" style="left:12px;top:1804px">Load More</div>

  <!-- markets -->
  <section class="abs" style="left:0;top:1860px;width:161px;height:430px;background:var(--soft)">
    <h2 class="abs sec-title" style="left:0;width:161px;top:22px;text-align:center;font-size:7px">Our <span class="blue">Markets</span></h2>
    <div class="abs" style="left:12px;top:48px;width:137px;display:flex;justify-content:space-between">
      <div><div class="m-icon"><span></span></div><div class="m-label">Auto</div></div>
      <div><div class="m-icon"><span></span></div><div class="m-label">Commercial</div></div>
      <div><div class="m-icon"><span></span></div><div class="m-label">Dental<br>Insurance</div></div>
    </div>
    <div class="abs" style="left:38px;top:96px;width:85px;display:flex;justify-content:space-between">
      <div><div class="m-icon"><span></span></div><div class="m-label">Disability</div></div>
      <div><div class="m-icon"><span></span></div><div class="m-label">Group Health<br>Insurance</div></div>
    </div>
    <div class="abs" style="left:45px;top:150px;width:70px;height:70px;border-radius:50%;background:#fff;border:1.5px solid var(--blue);display:flex;align-items:center;justify-content:center"><span class="head-font" style="font-weight:800;color:var(--blue);font-size:7px;text-align:center;line-height:1">CALM<br>HARBOR</span></div>
    <div class="abs" style="left:12px;top:240px;width:137px;display:flex;justify-content:space-between">
      <div><div class="m-icon"><span></span></div><div class="m-label">Homeowners</div></div>
      <div><div class="m-icon"><span></span></div><div class="m-label">Individual/Family<br>Health Insurance</div></div>
      <div><div class="m-icon"><span></span></div><div class="m-label">Medicare<br>Advantage</div></div>
    </div>
    <div class="abs" style="left:38px;top:292px;width:85px;display:flex;justify-content:space-between">
      <div><div class="m-icon"><span></span></div><div class="m-label">Medicare<br>Supplements</div></div>
      <div><div class="m-icon"><span></span></div><div class="m-label">Pension &amp;<br>Annuities</div></div>
    </div>
  </section>

  <!-- contact -->
  <section class="abs" style="left:0;top:2290px;width:161px;height:560px">
    <h2 class="abs sec-title" style="left:0;width:161px;top:26px;text-align:center;font-size:7px">Contact <span class="blue">Us</span></h2>
    <div class="abs" style="left:12px;top:50px;display:flex;gap:5px"><svg width="12" height="12" style="color:var(--orange)"><use href="#i-pin"/></svg><div style="font-size:4px;color:var(--muted);line-height:5.5px"><b style="color:var(--ink)">LOCATION:</b><br>410 Harbor Lane<br>Seaview, FL 33000</div></div>
    <div class="abs" style="left:12px;top:78px;display:flex;gap:5px"><svg width="12" height="12" style="color:var(--orange)"><use href="#i-phone"/></svg><div style="font-size:4px;color:var(--muted);line-height:5.5px"><b style="color:var(--ink)">PHONE:</b><br>954-555-0187</div></div>
    <div class="abs" style="left:12px;top:102px;display:flex;gap:5px"><svg width="12" height="12" style="color:var(--orange)"><use href="#i-mail"/></svg><div style="font-size:4px;color:var(--muted);line-height:5.5px"><b style="color:var(--ink)">EMAIL:</b><br>info@calmharborcover.com</div></div>
    <div class="abs" style="left:12px;top:140px;width:137px">
      <div style="font-size:4.6px;font-weight:700">GET IN TOUCH</div>
      <div style="font-size:4px;color:var(--muted);margin-bottom:8px">Reach out to us for any inquiry</div>
      <div class="m-field" style="margin-bottom:17px">First Name</div>
      <div class="m-field" style="margin-bottom:17px">Phone Number</div>
      <div class="m-field" style="margin-bottom:17px">Email Address</div>
      <div class="m-field" style="height:30px;margin-bottom:14px">Message</div>
      <div class="btn">Submit</div>
    </div>
    <div class="photo" role="img" aria-label="Street map showing the office location" style="left:12px;top:372px;width:137px;height:115px;background:linear-gradient(135deg,#eef1ec,#e4e9e1 50%,#dfe6ee);border:3px solid #fff;box-shadow:0 1px 6px rgba(0,0,0,.12)"></div>
  </section>

  <!-- doctors -->
  <section class="abs" style="left:0;top:2850px;width:161px;height:90px;background:var(--soft)">
    <h2 class="abs sec-title" style="left:0;width:161px;top:24px;text-align:center;font-size:6px">Doctors <span class="blue">Network</span></h2>
    <div class="abs" style="left:14px;top:44px;display:flex;gap:8px">
      <div class="partner" style="width:42px;height:24px"><span style="width:26px;height:7px;background:#f0a2a9"></span></div>
      <div class="partner" style="width:42px;height:24px"><span style="width:26px;height:7px;background:#3a3a3a"></span></div>
    </div>
    <div class="abs" style="left:72px;top:76px;display:flex;gap:3px"><i style="width:3px;height:3px;border-radius:50%;background:var(--ink)"></i><i style="width:3px;height:3px;border-radius:50%;background:#bbb"></i><i style="width:3px;height:3px;border-radius:50%;background:#bbb"></i></div>
  </section>

  <!-- footer -->
  <footer class="abs" style="left:0;top:2940px;width:161px;height:440px">
    <svg class="abs" style="left:0;top:0" width="161" height="440" viewBox="0 0 161 440" preserveAspectRatio="none"><rect width="161" height="440" fill="var(--soft)"/><path d="M0 14 C50 0 100 24 161 6 L161 440 L0 440Z" fill="var(--orange)"/><path d="M0 20 C50 6 100 30 161 12 L161 440 L0 440Z" fill="var(--blue)"/></svg>
    <div class="abs nav-logo" style="left:12px;top:40px;font-size:7px;color:#fff;flex-direction:column;align-items:flex-start;gap:3px"><span class="mark" style="width:12px;height:12px;background:#fff"></span>CALM<br>HARBOR</div>
    <div class="abs social" style="left:12px;top:76px;gap:3px"><i style="width:7px;height:7px"></i><i style="width:7px;height:7px"></i><i style="width:7px;height:7px"></i><i style="width:7px;height:7px"></i></div>
    <div class="abs foot-col" style="left:12px;top:100px"><h4 style="font-size:4.6px;margin-bottom:5px">Quick Links</h4><p style="font-size:4px;line-height:6.5px">Home<br>About Us<br>What We Do<br>Our Services<br>Doctors Network<br>Contact Us</p></div>
    <div class="abs foot-col" style="left:12px;top:186px"><h4 style="font-size:4.6px;margin-bottom:5px">About Company</h4><p style="font-size:4px;line-height:6.5px">Legal Information<br>Terms &amp; Condition<br>Privacy Policy<br>Support<br>Site Map<br>FAQ</p></div>
    <div class="abs foot-col" style="left:12px;top:276px;width:137px"><h4 style="font-size:4.6px;margin-bottom:5px">Contact Us</h4><p style="font-size:4px;line-height:6.5px"><b style="color:#fff">Phone</b><br>(813) 555-0166<br><b style="color:#fff">Email</b><br>info@calmharborcover.com<br><b style="color:#fff">Location</b><br>88 Pier Street, Seaview,<br>FL 33000</p></div>
    <div class="abs" style="left:0;width:161px;top:396px;text-align:center;font-size:4px;color:#dbe6f5;line-height:6px">2021 Copyright - calmharborcover.com<br>All Rights Reserved</div>
    <div class="abs" style="left:148px;top:420px;width:9px;height:9px;border-radius:50%;background:var(--orange)"></div>
  </footer>
</main>

</body>
</html>
```